Master Banner files - Square, Wide/Leaderboard, Tall/Skyscraper

I want you to design 9 master files for banners - so I can have them resized by junior graphic designers after this gig.
Banner 1 - Square - PEAK FORGE
Banner 2 - Wide - PEAK FORGE
Banner 3 - Tall - PEAK FORGE
Banner 4 - Square - TORCH CRATE
Banner 5 - Wide - TORCH CRATE
Banner 6 - Tall - TORCH CRATE
Banner 7 - Square - ONYX BUNDLE
Banner 8 - Wide - ONYX BUNDLE
Banner 9 - Tall - ONYX BUNDLE
Guidance for PEAK FORGE:
The info I need on this banner:
Logo
Text: PEAK FORGE
Text:
SUPERCHARGE
+ SIZE
+ STRENGTH
+ POWER
Text:
BUY 2 STACKS GET 3RD FREE
Text:
POWERFUL MUSCLE BUILDING FORMULA
LEGAL & 100% NATURAL
Button:
MORE INFO
Guidance for TORCH CRATE:
Logo
Text: TORCH CRATE
Text:
BURN FAT LIKE THE PROS
+ KEEP STRENGTH
+ KEEP SIZE
+ KEEP ENERGISED
+ STRIP FAT
Text:
BUY 2 STACKS GET 3RD FREE
Text:
THE MOST POWERFUL SUPPLEMENTS
LEGAL & 100% NATURAL
Button:
MORE INFO
The models you can use, the competitor banners can be found in the attachments, alongside logo - feel free to use your own models
Guidance for ONYX BUNDLE:
Logo
Text: ONYX BUNDLE
Text:
ENTER BEAST MODE
+ SIZE
+ STRENGTH
+ PERFORMANCE
Text:
BUY 2 STACKS GET 3RD FREE
Text:
GET INSANE RESULTS
LEGAL & 100% NATURAL
Button:
MORE INFO
Design Brief:
Use Black and white colour theme
Text: Roboto Condensed
Use theme in line with website theme: www.brevolantix.com
Competitor examples
Models
Logo
https://files.quorvenda.net/share/7KxPmW2rTzQe4LbN9aYdVh3sJ8cUf5oR?mode=view

```html
<!DOCTYPE html>
<html lang="en">
<head>
<meta charset="utf-8">
<title>PEAK FORGE – Banner Set</title>
<link rel="stylesheet" href="https://fonts.googleapis.com/css2?family=Roboto+Condensed:ital,wght@0,400;0,700;1,700&display=swap">
<style>
  :root {
    --canvas: #000000;
    --panel: #050505;
    --frame: #e6e6e6;
    --yellow: #f7c600;
    --white: #ffffff;
    --soft-white: #f0ece8;
    --btn-top: #ffd23a;
    --btn-bottom: #ff9f00;
  }
  * { margin: 0; padding: 0; box-sizing: border-box; }
  html, body {
    width: 1200px; height: 1200px; overflow: hidden;
    background: var(--canvas);
    font-family: "Roboto Condensed", "Arial Narrow", sans-serif;
  }
  .canvas { position: relative; width: 1200px; height: 1200px; }
  .banner {
    position: absolute; overflow: hidden;
    background: var(--panel);
    border: 2px solid var(--frame);
  }
  .banner--square { left: 35px; top: 46px; width: 695px; height: 695px; }
  .banner--tall { left: 747px; top: 35px; width: 408px; height: 723px; }
  .banner--wide { left: 35px; top: 784px; width: 1133px; height: 382px; }

  .photo { position: absolute; inset: 0; width: 100%; height: 100%; }

  .brand { position: absolute; display: flex; flex-direction: column; align-items: center; transform: translateX(-50%); }
  .brand__mark { border: 3px solid var(--white); border-radius: 50%; }
  .brand__name { color: var(--white); font-weight: 700; letter-spacing: 1px; margin-top: 8px; white-space: nowrap; }

  .title {
    position: absolute; color: var(--yellow); font-weight: 700; font-style: italic;
    line-height: 1; letter-spacing: -0.5px; white-space: nowrap;
  }
  .benefits { position: absolute; color: var(--white); font-weight: 700; list-style: none; white-space: nowrap; }
  .offer { position: absolute; color: var(--white); font-weight: 700; white-space: nowrap; }
  .claim {
    position: absolute; color: var(--yellow); font-style: italic; font-weight: 700;
    text-align: center; white-space: nowrap; transform: translateX(-50%);
  }
  .cta {
    position: absolute; display: flex; align-items: center; justify-content: center;
    border-radius: 999px; color: var(--white); font-weight: 700;
    background: linear-gradient(180deg, var(--btn-top), var(--btn-bottom));
    box-shadow: 0 0 0 2px rgba(255, 190, 0, 0.35);
  }

  /* Square */
  .banner--square .brand { left: 89px; top: 38px; }
  .banner--square .brand__mark { width: 72px; height: 72px; }
  .banner--square .brand__name { font-size: 22px; }
  .banner--square .title { left: 197px; top: 50px; font-size: 68px; }
  .banner--square .benefits { left: 249px; top: 320px; font-size: 30px; line-height: 42px; color: var(--soft-white); }
  .banner--square .offer { left: 110px; top: 494px; font-size: 31px; }
  .banner--square .claim { left: 308px; top: 540px; font-size: 22px; line-height: 28px; }
  .banner--square .cta { left: 250px; top: 611px; width: 149px; height: 54px; font-size: 26px; }

  /* Tall */
  .banner--tall .brand { left: 83px; top: 11px; }
  .banner--tall .brand__mark { width: 78px; height: 78px; }
  .banner--tall .brand__name { font-size: 22px; }
  .banner--tall .title { left: 35px; top: 308px; font-size: 66px; }
  .banner--tall .benefits { left: 113px; top: 377px; font-size: 30px; line-height: 45px; }
  .banner--tall .offer { left: 49px; top: 558px; font-size: 27px; }
  .banner--tall .claim { left: 197px; top: 601px; font-size: 18px; line-height: 21px; }
  .banner--tall .cta { left: 120px; top: 651px; width: 162px; height: 59px; font-size: 29px; }

  /* Wide */
  .banner--wide .brand { left: 1001px; top: 20px; }
  .banner--wide .brand__mark { width: 95px; height: 95px; }
  .banner--wide .brand__name { font-size: 28px; }
  .banner--wide .title { left: 58px; top: 17px; font-size: 72px; line-height: 62px; }
  .banner--wide .benefits { left: 58px; top: 154px; font-size: 29px; line-height: 38px; }
  .banner--wide .offer { left: 45px; top: 326px; font-size: 29px; }
  .banner--wide .claim { left: 934px; top: 230px; font-size: 22px; line-height: 26px; }
  .banner--wide .cta { left: 869px; top: 292px; width: 138px; height: 52px; font-size: 25px; }
</style>
</head>
<body>
<main class="canvas">

  <section class="banner banner--square">
    <svg class="photo" viewBox="0 0 695 695" role="img" aria-label="Photo of a muscular shirtless man curling a dumbbell in a gym">
      <defs>
        <linearGradient id="squarePhoto" x1="0" y1="0" x2="1" y2="1">
          <stop offset="0" stop-color="#3a2a2c"/>
          <stop offset="0.45" stop-color="#a07a78"/>
          <stop offset="1" stop-color="#2a1f20"/>
        </linearGradient>
      </defs>
      <polygon points="0,218 695,82 695,470 250,695 0,695" fill="url(#squarePhoto)"/>
    </svg>
    <div class="brand">
      <span class="brand__mark"></span>
      <span class="brand__name">BRAWNLEY</span>
    </div>
    <h1 class="title">PEAK FORGE</h1>
    <ul class="benefits">
      <li>SUPERCHARGE</li>
      <li>+ SIZE</li>
      <li>+ STRENGTH</li>
      <li>+ POWER</li>
    </ul>
    <p class="offer">BUY 2 STACKS GET 3RD FREE</p>
    <p class="claim">POWERFUL MUSCLE BUILDING FORMULA<br>LEGAL &amp; 100% NATURAL</p>
    <a class="cta">MORE INFO</a>
  </section>

  <section class="banner banner--tall">
    <svg class="photo" viewBox="0 0 408 723" role="img" aria-label="Black and white photo of a muscular man lifting a dumbbell">
      <defs>
        <linearGradient id="tallPhoto" x1="0" y1="0" x2="1" y2="1">
          <stop offset="0" stop-color="#1a1a1a"/>
          <stop offset="0.5" stop-color="#8a8a8a"/>
          <stop offset="1" stop-color="#222222"/>
        </linearGradient>
      </defs>
      <polygon points="0,0 408,0 408,300 0,400" fill="url(#tallPhoto)"/>
    </svg>
    <div class="brand">
      <span class="brand__mark"></span>
      <span class="brand__name">BRAWNLEY</span>
    </div>
    <h1 class="title">PEAK FORGE</h1>
    <ul class="benefits">
      <li>SUPERCHARGE</li>
      <li>+ SIZE</li>
      <li>+ STRENGTH</li>
      <li>+ POWER</li>
    </ul>
    <p class="offer">BUY 2 STACKS GET 3RD FREE</p>
    <p class="claim">POWERFUL MUSCLE BUILDING FORMULA<br>LEGAL &amp; 100% NATURAL</p>
    <a class="cta">MORE INFO</a>
  </section>

  <section class="banner banner--wide">
    <svg class="photo" viewBox="0 0 1133 382" role="img" aria-label="Photo of a man pressing dumbbells on a bench in front of a weight rack">
      <defs>
        <linearGradient id="widePhoto" x1="0" y1="0" x2="1" y2="1">
          <stop offset="0" stop-color="#1c1c1c"/>
          <stop offset="0.55" stop-color="#7a5a44"/>
          <stop offset="1" stop-color="#1a1410"/>
        </linearGradient>
      </defs>
      <polygon points="290,0 830,0 930,382 420,382" fill="url(#widePhoto)"/>
    </svg>
    <h1 class="title">PEAK<br>FORGE</h1>
    <ul class="benefits">
      <li>SUPERCHARGE</li>
      <li>+ SIZE</li>
      <li>+ STRENGTH</li>
      <li>+ POWER</li>
    </ul>
    <p class="offer">BUY 2 STACKS GET 3RD FREE</p>
    <div class="brand">
      <span class="brand__mark"></span>
      <span class="brand__name">BRAWNLEY</span>
    </div>
    <p class="claim">POWERFUL MUSCLE BUILDING FORMULA<br>LEGAL &amp; 100% NATURAL</p>
    <a class="cta">MORE INFO</a>
  </section>

</main>
</body>
</html>
```